Financial Advisor needs waiting room sign

I am a financial advisor that works with a number of accountants to develop prospects. I am looking for a 18"x24" sign to hang in their office waiting rooms to help develop prospect interest in my services. My original idea was to list all of our services in a jumbled way on the sign and on the bottom have something like "Confused? We have the answers?" "Questions - We have answers" Our logo on the bottom. While I think this is still a good idea when I try to design it - it does not work. I am open to other ideas. Here is a list of our services (list in no particular order) and I will attach our logo. List: Plovance, Plovance Supplement, Plovance Advantage, Truvely, Part A, Part B, Part D, Social Security, Turning 65, Annuities, Fixed Index Annuities, Rollovers, 401k, 403b, Investments, Stock Market, Mutual Funds, Term Insurance, Life Insurance, Final Expense, Long Term Care, Mortgage Protection, 403B / 457 Not for Profit Set Up, 403B / TSA Plans, Annuities, Asset Protection, Charitable Giving, College Funding, Estate Planning, Fixed Indexed Annuities, Guaranteed Income, IRA & 401(K) Assets and Planning, IRA, 401(K), 403(B) Rollovers, Lifetime Income Planning, Retirement Income Planning, Safe Money Options, Social Security, Tactical Asset Allocation

```html
<!DOCTYPE html>
<html lang="en">
<head>
<meta charset="utf-8">
<title>We have the answers – Brenwick Capital</title>
<link rel="stylesheet" href="https://fonts.googleapis.com/css2?family=Gelasio:wght@700&display=swap">
<style>
  :root {
    --sign-red: #f80423;
    --headline-green: #12e61c;
    --service-yellow: #f8e043;
    --badge-white: #ffffff;
    --brand-green: #4d7414;
  }
  html, body {
    margin: 0;
    padding: 0;
    overflow: hidden;
  }
  .sign {
    position: relative;
    width: 900px;
    height: 1200px;
    background: var(--sign-red);
    overflow: hidden;
    font-family: "Gelasio", Georgia, serif;
    font-weight: 700;
  }
  .headline {
    position: absolute;
    top: 20px;
    left: 0;
    width: 100%;
    margin: 0;
    text-align: center;
    font-size: 55px;
    line-height: 72px;
    letter-spacing: 0.3px;
    color: var(--headline-green);
  }
  .service-list {
    position: absolute;
    top: 110px;
    left: 229px;
    margin: 0;
    padding: 0;
    list-style: none;
    font-size: 25.5px;
    line-height: 29.2px;
    color: var(--service-yellow);
    white-space: nowrap;
  }
  .brand-badge {
    position: absolute;
    left: 239px;
    top: 1077px;
    width: 422px;
    height: 81px;
    background: var(--badge-white);
    display: flex;
    align-items: center;
    justify-content: center;
    gap: 16px;
  }
  .brand-dot {
    width: 44px;
    height: 44px;
    border-radius: 50%;
    background: var(--brand-green);
  }
  .brand-name {
    font-size: 30px;
    color: var(--brand-green);
    letter-spacing: 1px;
  }
</style>
</head>
<body>
  <main class="sign">
    <h1 class="headline">We have the answers</h1>
    <ul class="service-list">
      <li>Plovance,</li>
      <li>Plovance Supplement,</li>
      <li>Plovance Advantage,</li>
      <li>Truvely, Part A, Part B, Part D,</li>
      <li>Social Security,</li>
      <li>Turning 65,</li>
      <li>Annuities,</li>
      <li>Fixed Index Annuities,</li>
      <li>Rollovers, 401k, 403b,</li>
      <li>Investments, Stock</li>
      <li>Market,</li>
      <li>Mutual Funds,</li>
      <li>Term Insurance,</li>
      <li>Life Insurance,</li>
      <li>Final Expense,</li>
      <li>Long Term Care,</li>
      <li>Mortgage Protection,</li>
      <li>403B / 457 Not for Profit Set Up,</li>
      <li>403B / TSA Plans,</li>
      <li>Annuities,</li>
      <li>Asset Protection,</li>
      <li>Charitable Giving,</li>
      <li>College Funding,</li>
      <li>Estate Planning,</li>
      <li>Fixed Indexed Annuities,</li>
      <li>Guaranteed Income,</li>
      <li>IRA &amp; 401(K) Assets and Planning,</li>
      <li>IRA, 401(K), 403(B) Rollovers,</li>
      <li>Lifetime Income Planning,</li>
      <li>Retirement Income Planning,</li>
      <li>Safe Money Options, Social Security,</li>
      <li>Tactical Asset Allocation</li>
    </ul>
    <div class="brand-badge">
      <span class="brand-dot" aria-hidden="true"></span>
      <span class="brand-name">Brenwick Capital</span>
    </div>
  </main>
</body>
</html>
```